The Corvel Dental centre, the Zorvik of dentistry

New concept of running a dental practice by having a walk in practice
WE ARE A HUSBAND AND WIFE TEAM

Really modern and sophisticated, we want it to feel different from the traditional dental practice.
we want it split into different pages:CONTACT US
LOCATION: Information about our location since patients often confuse us with the practice across the road
ABOUT US:
Opening hours - & 7 Days, We offer a weekend service
WALK IN: We offer a walk in service for dental treatments
TREATMENTS we offer

DENTAL ADVICE: Free dentist advise call back- So a dentist will call you back for free to discuss

Target Market(s)

Everyone

Industry/Entity Type

Dental

Coding

Coded - Design and coding required

Number of Pages Required

5+ page

Requirements
Must have
• First page
• * changing pictures
• *opening times
• * our walk in concept I.e. no appointment needed
• *logo
• * links in to medi portal (online booking system in Australia)
• * address /phone number/email
• * possible videos
• Second page
• meet the team
• third page
• dental treatments/walk in treatments
• fourth page
• dental advice with you tube videos
• Fifth page
• contact us/maps/ we get confused with the dental practice across the road
• We would also like a giving back page. In this please include the photo's below of our dental mission in Guatemala, where by we did treatment for patients as part of a charity.
Nice to have
• Changing pictures on the home screen
• videos linked to home page

```html
<!DOCTYPE html>
<html lang="en">
<head>
<meta charset="utf-8">
<title>The Corvel Dental centre</title>
<link href="https://fonts.googleapis.com/css2?family=Open+Sans:wght@300;400;600;700&display=swap" rel="stylesheet">
<style>
:root{
  --green:#8dc63f;
  --green-dark:#76ad2d;
  --blue:#1b9ce0;
  --blue-light:#5bbcf0;
  --navy:#1f3b57;
  --text:#444;
  --muted:#8a8a8a;
  --white:#fff;
  --line:#e3e3e3;
}
*{margin:0;padding:0;box-sizing:border-box}
html,body{width:800px;height:1200px;overflow:hidden}
body{font-family:"Open Sans",Arial,sans-serif;color:var(--text);background:var(--white);position:relative}
.wrap{width:684px;margin:0 auto;position:relative}

/* header */
.site-header{height:93px;display:flex;align-items:center;justify-content:space-between;padding:0 58px}
.brand{display:flex;align-items:center;gap:10px}
.brand-dot{width:34px;height:34px;border-radius:50%;background:var(--blue-light)}
.brand-name{font-size:20px;font-weight:600;color:var(--blue);line-height:1.05}
.brand-name small{display:block;font-size:10px;letter-spacing:3px;font-weight:600;color:var(--blue)}
.header-contact{text-align:right}
.header-contact .note{font-size:11px;color:var(--green-dark);font-weight:600}
.header-contact .note span{color:var(--muted);font-weight:400}
.header-contact .phone{font-size:22px;color:var(--navy);font-weight:600;letter-spacing:.5px}

/* nav */
.main-nav{background:var(--green);height:19px}
.main-nav ul{list-style:none;display:flex;width:684px;margin:0 auto}
.main-nav li{font-size:9px;color:var(--white);padding:0 12px;line-height:19px;border-right:1px solid rgba(255,255,255,.5)}
.main-nav li.active{background:var(--green-dark)}

/* hero */
.hero{margin-top:13px;height:208px;display:flex;background:var(--blue-light)}
.hero-text{width:290px;padding:50px 0 0 40px;color:var(--white)}
.hero-text h1{font-size:40px;font-weight:600;line-height:1}
.hero-text p{font-size:19px;font-weight:300;line-height:1.2;margin-top:4px}
.hero-text p.navy{color:var(--navy)}
.hero-photo{flex:1;background:linear-gradient(120deg,#9ed6f3 0%,#e8eef0 45%,#d9c2a8 100%)}

/* cards */
.features{margin-top:14px;display:flex;gap:12px;height:226px}
.card{flex:1;position:relative;overflow:hidden}
.card-green{background:var(--green);color:var(--white)}
.card-blue{background:var(--blue);color:var(--white)}
.card h2{font-size:19px;font-weight:300;line-height:1.15;text-align:center;padding:14px 10px 0}
.card .photo{height:78px;margin:10px 0}
.card-green .photo{background:linear-gradient(90deg,#dfe9f1,#b7d6ea)}
.card-blue .photo{background:linear-gradient(90deg,#f2d9c6,#c8dff0)}
.card p{font-size:8px;text-align:center;padding:0 18px;line-height:1.5}
.card p + p{margin-top:8px}
.card-team{background:linear-gradient(180deg,#cfd6dc,#8c7a6c)}
.team-caption{position:absolute;left:0;right:0;bottom:0;background:rgba(255,255,255,.88);padding:8px 12px}
.team-caption h3{font-size:15px;font-weight:600;color:var(--navy)}
.team-caption p{font-size:8px;text-align:left;padding:0;color:var(--text)}

/* quote */
.quote{margin-top:36px;text-align:center;position:relative;height:48px}
.quote p{font-size:14px;font-style:italic;color:var(--muted)}
.quote cite{display:block;font-size:12px;font-style:normal;font-weight:700;color:var(--navy);margin-top:2px}
.quote svg{position:absolute;top:-4px}

/* testimonials */
.testimonials{position:absolute;top:688px;left:0;width:800px;height:205px;background:var(--green)}
.testimonials h2{color:var(--white);text-align:center;font-size:24px;font-weight:400;letter-spacing:1px;padding-top:12px}
.testimonials h2::before,.testimonials h2::after{content:"";display:inline-block;width:150px;height:1px;background:rgba(255,255,255,.7);vertical-align:middle;margin:0 14px}
.testimonial-row{display:flex;gap:30px;width:684px;margin:22px auto 0}
.testimonial{flex:1;display:flex;gap:12px}
.avatar{width:70px;height:70px;border-radius:50%;flex:none;border:3px solid var(--white)}
.avatar-a{background:linear-gradient(180deg,#d7c0a8,#9a7a60)}
.avatar-b{background:linear-gradient(180deg,#e6cdb4,#b08a6a)}
.testimonial .date{font-size:8px;font-weight:700;color:var(--white)}
.testimonial p{font-size:8px;color:var(--white);line-height:1.55;margin-top:4px}

/* mission */
.mission{position:absolute;top:893px;left:0;width:800px;height:240px;background:var(--blue)}
.mission h2{color:var(--white);text-align:center;font-size:24px;font-weight:600;padding-top:10px}
.mission-photo{width:446px;height:168px;margin:10px auto 0;border:3px solid var(--green);background:linear-gradient(180deg,#d9dde0 0%,#6c93b8 55%,#3f6b94 100%)}

/* footer */
.site-footer{position:absolute;top:1160px;left:0;width:800px;border-top:1px solid var(--line);padding-top:10px}
.site-footer ul{list-style:none;display:flex;justify-content:center}
.site-footer li{font-size:8px;color:var(--muted);padding:0 12px;border-right:1px solid var(--line)}
.site-footer li:last-child{border:none}
</style>
</head>
<body>
<header class="site-header">
  <div class="brand">
    <div class="brand-dot"></div>
    <div class="brand-name">The Corvel<small>DENTAL CENTRE</small></div>
  </div>
  <div class="header-contact">
    <div class="note">Walk in appointments available, <span>call today to find out more</span></div>
    <div class="phone">0198-765-4321</div>
  </div>
</header>

<nav class="main-nav">
  <ul>
    <li class="active">Home</li>
    <li>Meet Our Team</li>
    <li>Dental treatments/Walk-in treatments</li>
    <li>Dental advice</li>
    <li>Contact Us</li>
  </ul>
</nav>

<main class="wrap">
  <section class="hero">
    <div class="hero-text">
      <h1>Nervous,</h1>
      <p>don't worry we can help relieve your fears,</p>
      <p class="navy">come in and have a chat with our friendly dentists.</p>
    </div>
    <div class="hero-photo" role="img" aria-label="Smiling child in a dental chair with a dentist"></div>
  </section>

  <section class="features">
    <article class="card card-green">
      <h2>Weekend &amp; Emergency Appointments</h2>
      <div class="photo" role="img" aria-label="Clinic treatment room"></div>
      <p>Weekend and emergency appointments available</p>
      <p>Call our office today</p>
    </article>
    <article class="card card-blue">
      <h2>New Patient Specials</h2>
      <div class="photo" role="img" aria-label="Patient smiling during a check-up"></div>
      <p>Free new patient consultation for all booked patients. Over the holidays we are open daily</p>
      <p>Walk in and register</p>
    </article>
    <article class="card card-team" role="img" aria-label="Portrait of the two dentists">
      <div class="team-caption">
        <h3>Lena and Ravi</h3>
        <p>We want our patients to feel safe, happy and have dental treatment which is affordable.</p>
      </div>
    </article>
  </section>

  <blockquote class="quote">
    <svg style="left:110px" width="18" height="14" viewBox="0 0 18 14"><path d="M0 14V8C0 3 3 0 7 0v3C5 3 4 5 4 7h3v7zM11 14V8c0-5 3-8 7-8v3c-2 0-3 2-3 4h3v7z" fill="#1b9ce0"/></svg>
    <p>A dentist at work in his vocation always looks down in the mouth.</p>
    <cite>Harold M. Quill</cite>
    <svg style="right:110px" width="18" height="14" viewBox="0 0 18 14"><path d="M18 0v6c0 5-3 8-7 8v-3c2 0 3-2 3-4h-3V0zM7 0v6c0 5-3 8-7 8v-3c2 0 3-2 3-4H0V0z" fill="#1b9ce0"/></svg>
  </blockquote>
</main>

<section class="testimonials">
  <h2>TESTIMONIALS</h2>
  <div class="testimonial-row">
    <div class="testimonial">
      <div class="avatar avatar-a" role="img" aria-label="Patient portrait"></div>
      <div>
        <div class="date">7 November 2015</div>
        <p>Walking in without an appointment was so easy. The team were calm and kind, and explained every step before they started. I left with a smile and no fear at all. Highly recommended to my family.</p>
      </div>
    </div>
    <div class="testimonial">
      <div class="avatar avatar-b" role="img" aria-label="Patient portrait"></div>
      <div>
        <div class="date">6 June 2015</div>
        <p>I was nervous for years, but the dentists here took their time and listened. Weekend opening made it simple to come in. Friendly staff, fair prices and a bright, modern clinic.</p>
      </div>
    </div>
  </div>
</section>

<section class="mission">
  <h2>Dental Mission</h2>
  <div class="mission-photo" role="img" aria-label="Group photo of the volunteer dental mission team"></div>
</section>

<footer class="site-footer">
  <ul>
    <li>Home</li>
    <li>Meet Our Team</li>
    <li>Dental treatments/Walk-in treatments</li>
    <li>Dental advice</li>
    <li>Contact Us</li>
  </ul>
</footer>
</body>
</html>
```